Looking for a high-end business card design for a construction company

We are looking to update our business card design. We are a post-frame construction company that builds custom buildings, commercial spaces, homes, and anything else. We have multiple people working here so we would need something we can easily customize the information for the specific person. We need a name, website, cell phone, office phone as well as social icons. Our colors are black, white, and grey/silver so I would love a black background or something that is more striking than just a traditional white business card. Looking for something that is very professional with a high-end look/feel. I have attached our logos, they can be silver, white, grey, or black.
Industry/Entity Type
Construction
Contact Information for Business Card
Business logo, Name, Cell phone, Office phone, website, social Icons
Colors
Designer to choose only greyscale colors for use in the design.
Look and feel

```html
<!DOCTYPE html>
<html lang="en">
<head>
<meta charset="utf-8">
<title>Harwick Builders – Business Card</title>
<link rel="stylesheet" href="https://fonts.googleapis.com/css2?family=Open+Sans:ital,wght@0,400;0,700;1,400&display=swap">
<style>
  :root {
    --stage: #2a2a2a;
    --card-white: #ffffff;
    --card-black: #111111;
    --ink: #141414;
    --ink-soft: #5a5a5a;
    --rule: #3a3a3a;
    --silver: #9a9a9a;
  }
  * { box-sizing: border-box; margin: 0; padding: 0; }
  html, body {
    width: 1200px; height: 900px; overflow: hidden;
    background: var(--stage);
    font-family: "Open Sans", sans-serif;
  }
  .canvas {
    width: 1200px; height: 900px;
    display: flex; flex-direction: column;
    align-items: center; justify-content: center; gap: 60px;
  }
  .card {
    width: 630px; height: 360px;
    position: relative;
    box-shadow: 0 14px 30px rgba(0,0,0,.45);
  }
  /* Front */
  .card-front {
    background: var(--card-white);
    display: flex; align-items: center;
  }
  .brand {
    width: 330px;
    display: flex; align-items: center; justify-content: center; gap: 12px;
  }
  .brand-mark {
    width: 22px; height: 22px; border-radius: 50%;
    background: var(--ink);
    flex: none;
  }
  .brand-name {
    font-weight: 700; font-size: 24px; line-height: 1.1;
    letter-spacing: .08em; text-transform: uppercase;
    color: var(--ink);
  }
  .divider {
    width: 1px; height: 150px; background: var(--rule);
    flex: none;
  }
  .contact {
    padding-left: 28px;
    color: var(--ink-soft);
  }
  .person-name {
    font-weight: 700; font-size: 21px; letter-spacing: .02em;
    text-transform: uppercase; color: var(--ink);
  }
  .person-title {
    font-size: 15px; margin-bottom: 10px;
  }
  .contact-list { list-style: none; }
  .contact-item {
    display: flex; align-items: center; gap: 9px;
    font-size: 15px; line-height: 22px;
  }
  .contact-icon { width: 12px; height: 12px; flex: none; fill: var(--ink); }
  /* Back */
  .card-back {
    background: var(--card-black);
    display: flex; align-items: center; justify-content: center; gap: 14px;
  }
  .card-back .brand-mark { background: var(--silver); width: 26px; height: 26px; }
  .card-back .brand-name { color: var(--silver); font-size: 30px; }
</style>
</head>
<body>
<main class="canvas">
  <section class="card card-front">
    <div class="brand">
      <span class="brand-mark"></span>
      <span class="brand-name">Harwick<br>Builders, Inc.</span>
    </div>
    <div class="divider"></div>
    <div class="contact">
      <p class="person-name">Daniel Orsett</p>
      <p class="person-title">President</p>
      <ul class="contact-list">
        <li class="contact-item">
          <svg class="contact-icon" viewBox="0 0 12 12" aria-hidden="true"><path d="M3 0h6a1 1 0 0 1 1 1v10a1 1 0 0 1-1 1H3a1 1 0 0 1-1-1V1a1 1 0 0 1 1-1zm.5 1.5v8h5v-8z"/></svg>
          555-318-4720
        </li>
        <li class="contact-item">
          <svg class="contact-icon" viewBox="0 0 12 12" aria-hidden="true"><path d="M2.4 0.6l1.8 0 .9 2.6-1.3 1a7 7 0 0 0 3 3l1-1.3 2.6.9v1.8a1.5 1.5 0 0 1-1.6 1.5A9.5 9.5 0 0 1 .9 2.2 1.5 1.5 0 0 1 2.4.6z"/></svg>
          555-318-4720
        </li>
        <li class="contact-item">
          <svg class="contact-icon" viewBox="0 0 12 12" aria-hidden="true"><path d="M0 2h12v.8L6 6.6 0 2.8zM0 4l6 3.8L12 4v6H0z"/></svg>
          dorsett@harwickbuilders
        </li>
        <li class="contact-item">
          <svg class="contact-icon" viewBox="0 0 12 12" aria-hidden="true"><path d="M6 0a6 6 0 1 0 0 12A6 6 0 0 0 6 0zm0 1.2c.8.8 1.3 2 1.5 3.3h-3C4.7 3.2 5.2 2 6 1.2zM1.3 5.5h2.1c0 1.3.4 2.5 1 3.5A4.8 4.8 0 0 1 1.3 5.5zm3.2 0h3c-.1 1.3-.7 2.5-1.5 3.3-.8-.8-1.4-2-1.5-3.3zm4.1 0h2.1a4.8 4.8 0 0 1-3.1 3.5c.6-1 1-2.2 1-3.5z"/></svg>
          www.harwickbuilders.com
        </li>
      </ul>
    </div>
  </section>

  <section class="card card-back">
    <span class="brand-mark"></span>
    <span class="brand-name">Harwick Builders</span>
  </section>
</main>
</body>
</html>
```